Organization and people consulting firm needs a website design

I need a website that promotes and explains the consulting service we will provide. The organization is called Lakemont Counsel Group. Our services include organization design, employee experience, change management, and executive coaching. I would like to see a simple clean and professional design, that reflects a modern and forward looking professional services company

Target Market(s)

Mid market and large companies

Industry/Entity Type

Management Consulting

Coding

Coded - Design and coding required

Number of Pages Required

5+ page

Font styles to use
Sans Serif

Colors

Designer to choose colors to be used in the design.

Requirements
Must have
• The following pages: Home, The Way We Work, What We Do, Our Founder, Insights, Contact.
• Search button.
• Hyper links (will be provided with main body text)
• Scrolling website with summaries at top level and links to more detail at lower level (like this website: brightvane.com)
• Company logo (uploaded)
• I have text for each of the pages that I can upload once the basic design is done
Should not have
• No clutter, keep the design clean

```html
<!DOCTYPE html>
<html lang="en">
<head>
<meta charset="utf-8">
<title>Lakemont Counsel Group</title>
<link rel="stylesheet" href="https://fonts.googleapis.com/css2?family=Montserrat:wght@300;400&family=Open+Sans:wght@400;600;700&family=Lato:wght@400&display=swap">
<style>
  :root {
    --ink: #333333;
    --body-text: #777777;
    --white: #ffffff;
    --soft-grey: #f8f8f8;
    --hero-dark: #1c1c1c;
    --hero-mid: #3a3a3a;
    --accent-red: #e2554f;
    --pill-grey: #d4d4d4;
    --footer-bg: #232323;
    --footer-text: #8a8a8a;
    --photo-tone: #b9b4ae;
  }
  * { box-sizing: border-box; margin: 0; padding: 0; }
  html, body { width: 1200px; height: 2703px; overflow: hidden; }
  body { background: var(--white); font-family: "Lato", sans-serif; color: var(--ink); }

  .hero {
    position: relative; height: 590px;
    background: radial-gradient(ellipse at 50% 35%, var(--hero-mid) 0%, var(--hero-dark) 70%, #0f0f0f 100%);
  }
  .site-header {
    position: absolute; top: 0; left: 0; right: 0; height: 82px;
    display: flex; align-items: center; justify-content: space-between;
    padding: 0 94px 0 66px;
  }
  .brand {
    font-family: "Open Sans", sans-serif; font-weight: 600; font-size: 21px;
    color: var(--white); letter-spacing: 0.5px;
    display: flex; align-items: center; gap: 10px;
  }
  .brand-mark { width: 14px; height: 14px; background: var(--white); border-radius: 50%; }
  .main-nav { display: flex; gap: 27px; }
  .main-nav a {
    font-family: "Open Sans", sans-serif; font-size: 14px; color: var(--white);
    text-decoration: none; letter-spacing: 0.3px;
  }
  .main-nav a.is-current { color: var(--accent-red); }

  .hero-content { position: absolute; top: 252px; left: 0; right: 0; text-align: center; }
  .hero-title {
    font-family: "Open Sans", sans-serif; font-weight: 600; font-size: 52px;
    color: var(--white); line-height: 64px; padding-left: 0;
  }
  .hero-subtitle {
    font-family: "Open Sans", sans-serif; font-size: 22px; color: var(--white);
    margin-top: 20px; line-height: 30px;
  }
  .hero-button {
    display: inline-flex; align-items: center; gap: 10px;
    margin-top: 34px; margin-right: 80px; height: 48px; padding: 0 30px;
    border-radius: 24px; background: var(--pill-grey); color: #222;
    font-family: "Open Sans", sans-serif; font-weight: 700; font-size: 15px; text-decoration: none;
  }

  .summary { text-align: center; }
  .summary--grey { background: var(--soft-grey); }
  .summary-title {
    font-family: "Montserrat", sans-serif; font-weight: 300; font-size: 34px;
    line-height: 40px; color: var(--ink);
  }
  .summary-text {
    width: 720px; margin: 14px auto 0; font-size: 16px; line-height: 35px; color: var(--body-text);
  }
  .outline-button {
    display: inline-flex; align-items: center; justify-content: center;
    height: 41px; border: 2px solid #111; color: #111; text-decoration: none;
    font-family: "Open Sans", sans-serif; font-weight: 700; font-size: 10px; letter-spacing: 2.6px;
  }
  .how-we-work { height: 375px; padding-top: 94px; }
  .what-we-do { height: 321px; padding-top: 47px; }
  .our-founder { height: 620px; padding-top: 74px; }
  .insights { height: 321px; padding-top: 48px; }
  .contact { height: 412px; padding-top: 75px; }
  .how-we-work .outline-button,
  .what-we-do .outline-button,
  .insights .outline-button { width: 180px; margin-top: 27px; }
  .founder-photo {
    width: 202px; height: 253px; margin: 25px auto 0;
    background: linear-gradient(180deg, #ecebe9 0%, var(--photo-tone) 55%, #2a2a2e 100%);
  }
  .our-founder .outline-button { width: 249px; margin-top: 28px; }
  .contact .outline-button { width: 187px; margin-top: 29px; }

  .site-footer {
    height: 64px; background: var(--footer-bg);
    display: flex; align-items: center; justify-content: space-between; padding: 0 78px 0 66px;
    font-family: "Open Sans", sans-serif; font-weight: 700; font-size: 9px; color: var(--footer-text);
  }
  .footer-nav { display: flex; gap: 16px; }
  .footer-nav a { color: var(--footer-text); text-decoration: none; }
</style>
</head>
<body>
  <header class="hero">
    <div class="site-header">
      <div class="brand"><span class="brand-mark"></span>Lakemont Counsel Group</div>
      <nav class="main-nav">
        <a href="#" class="is-current">HOME</a>
        <a href="#">HOW WE WORK</a>
        <a href="#">WHAT WE DO</a>
        <a href="#">OUR FOUNDER</a>
        <a href="#">INSIGHTS</a>
        <a href="#">CONTACT</a>
      </nav>
    </div>
    <div class="hero-content" role="img" aria-label="Dark textured concrete background">
      <h1 class="hero-title">Lakemont Counsel Group</h1>
      <p class="hero-subtitle">Building the Workforce and Organization of the Future</p>
      <a class="hero-button" href="#">Learn more
        <svg width="8" height="12" viewBox="0 0 8 12"><path d="M1.5 1.5 6 6l-4.5 4.5" fill="none" stroke="#222" stroke-width="2.2"/></svg>
      </a>
    </div>
  </header>

  <section class="summary how-we-work">
    <h2 class="summary-title">How we work</h2>
    <p class="summary-text">Insight development is not a mechanical process. One needs to acknowledge a certain level of uncertainty, and embrace the role of serendipity. Our way of working allows us to follow a systematic method while allowing for creativity and chance connections.</p>
    <a class="outline-button" href="#">LEARN MORE</a>
  </section>

  <section class="summary summary--grey what-we-do">
    <h2 class="summary-title">What We Do</h2>
    <p class="summary-text">Insight development is not a mechanical process. One needs to acknowledge a certain level of uncertainty, and embrace the role of serendipity. Our way of working allows us to follow a systematic method while allowing for creativity and chance connections.</p>
    <a class="outline-button" href="#">LEARN MORE</a>
  </section>

  <section class="summary our-founder">
    <h2 class="summary-title">Our founder</h2>
    <p class="summary-text">Daniel has over 30 years experience working with clients around the world and across a wide variety of industries on complex organizational and people issues.</p>
    <div class="founder-photo" role="img" aria-label="Portrait photo of the founder in a dark suit"></div>
    <a class="outline-button" href="#">MORE ABOUT DANIEL</a>
  </section>

  <section class="summary summary--grey insights">
    <h2 class="summary-title">Insights</h2>
    <p class="summary-text">Insight development is not a mechanical process. One needs to acknowledge a certain level of uncertainty, and embrace the role of serendipity. Our way of working allows us to follow a systematic method while allowing for creativity and chance connections.</p>
    <a class="outline-button" href="#">LEARN MORE</a>
  </section>

  <section class="summary contact">
    <h2 class="summary-title">Contact</h2>
    <p class="summary-text">Insight development is not a mechanical process. One needs to acknowledge a certain level of uncertainty, and embrace the role of serendipity. Our way of working allows us to follow a systematic method while allowing for creativity and chance connections.</p>
    <a class="outline-button" href="#">GET IN TOUCH</a>
  </section>

  <footer class="site-footer">
    <span>COPYRIGHT 2018 · LAKEMONT COUNSEL GROUP ALL RIGHTS RESERVED.</span>
    <nav class="footer-nav">
      <a href="#">HOME</a><a href="#">HOW WE WORK</a><a href="#">WHAT WE DO</a><a href="#">OUR FOUNDER</a><a href="#">INSIGHTS</a><a href="#">CONTACT</a>
    </nav>
  </footer>
</body>
</html>
```